Australian Software Consultancy needs new Business Card Design

Design Business Card based on existing design artefacts (attached). We are open to all designs. As its a 2 sided design and we thought it might be quite striking to have one side with a black background and te other side with a white background.

Target Market(s)

Financial Services mainly.

Industry/Entity Type

Business

Contact Information for Business Card

Name :
Position :
Email :

Requirements
Must have
• Funky design using our existing assets

```html
<!DOCTYPE html>
<html lang="en">
<head>
<meta charset="utf-8">
<title>North Lane – Business Card</title>
<link rel="stylesheet" href="https://fonts.googleapis.com/css2?family=Exo+2:wght@400;500;700;800&display=swap">
<style>
  :root {
    --stage: #000000;
    --card: #ffffff;
    --brand-red: #ec1c24;
    --ink: #111111;
    --pattern-tint: #fbeeee;
  }
  * { margin: 0; padding: 0; box-sizing: border-box; }
  html, body {
    width: 1200px; height: 900px; overflow: hidden;
    background: var(--stage);
    font-family: "Exo 2", sans-serif;
  }
  .canvas { position: relative; width: 1200px; height: 900px; }
  .card {
    position: absolute; top: 271px; width: 457px; height: 281px;
    background: var(--card); border-radius: 12px; overflow: hidden;
  }
  .card--front { left: 137px; }
  .card--back { left: 626px; }

  .brand { position: absolute; display: flex; align-items: center; gap: 10px; }
  .brand__mark {
    border: 4px solid var(--brand-red); border-radius: 50%;
  }
  .brand__name {
    color: var(--ink); font-weight: 700; letter-spacing: 1px; white-space: nowrap;
  }
  .card--front .brand { left: 28px; top: 29px; }
  .card--front .brand__mark { width: 52px; height: 52px; }
  .card--front .brand__name { font-size: 24px; }

  .identity-band {
    position: absolute; left: 0; top: 133px; width: 340px; height: 119px;
    background: var(--brand-red);
  }
  .identity-disc {
    position: absolute; left: 296px; top: 127px; width: 134px; height: 134px;
    border-radius: 50%; background: var(--card);
    border: 9px solid var(--brand-red);
  }
  .person { position: absolute; left: 26px; top: 145px; color: #fff; }
  .person__name { font-size: 20px; font-weight: 700; letter-spacing: 1px; line-height: 1.1; }
  .person__role { font-size: 12px; font-weight: 500; letter-spacing: .5px; margin-top: 3px; }
  .contact { position: absolute; left: 27px; top: 202px; list-style: none; color: #fff; font-size: 13px; }
  .contact li { display: flex; align-items: center; gap: 8px; height: 21px; }
  .contact svg { width: 13px; height: 13px; }

  .back-pattern {
    position: absolute; inset: 0; background: var(--pattern-tint);
  }
  .card--back .brand {
    left: 0; right: 0; top: 80px; flex-direction: column; gap: 12px;
  }
  .card--back .brand__mark { width: 80px; height: 80px; border-width: 5px; background: var(--card); }
  .card--back .brand__name { font-size: 28px; }
  .website {
    position: absolute; left: 0; right: 0; top: 233px; text-align: center;
    font-size: 12px; color: var(--ink); font-weight: 500;
  }
  .website span { color: var(--brand-red); }
</style>
</head>
<body>
<main class="canvas">
  <section class="card card--front" aria-label="Business card front">
    <div class="brand">
      <div class="brand__mark"></div>
      <div class="brand__name">NORTH LANE</div>
    </div>
    <div class="identity-band"></div>
    <div class="identity-disc"></div>
    <div class="person">
      <div class="person__name">AARON VALE</div>
      <div class="person__role">DIRECTOR</div>
    </div>
    <ul class="contact">
      <li>
        <svg viewBox="0 0 14 14" aria-hidden="true"><circle cx="7" cy="7" r="7" fill="#fff"/><path d="M4.2 3.8c.4-.3.9-.3 1.1.1l.7 1.2c.2.4.1.7-.2 1l-.4.3c.4.9 1.1 1.6 2 2l.3-.4c.3-.3.7-.4 1-.2l1.2.7c.4.2.4.7.1 1.1-.6.7-1.4.9-2.3.5-1.7-.7-3-2-3.7-3.7-.4-.9-.2-1.8.2-2.6z" fill="var(--brand-red)"/></svg>
        555- 014-2270
      </li>
      <li>
        <svg viewBox="0 0 14 14" aria-hidden="true"><circle cx="7" cy="7" r="7" fill="#fff"/><rect x="3.6" y="4.6" width="6.8" height="4.8" rx=".6" fill="var(--brand-red)"/><path d="M3.8 5l3.2 2.4L10.2 5" stroke="#fff" stroke-width=".8" fill="none"/></svg>
        hello@northlane.com
      </li>
    </ul>
  </section>

  <section class="card card--back" aria-label="Business card back">
    <div class="back-pattern" role="img" aria-label="Faint repeating brand pattern background"></div>
    <div class="brand">
      <div class="brand__mark"></div>
      <div class="brand__name">NORTH LANE</div>
    </div>
    <p class="website">www.<span>northlane.com</span></p>
  </section>
</main>
</body>
</html>
```